Brisbo Excavation and Landscaping

I need a double sided card thick with rounded edges. I want an identical card of one of your designs but with my name on it on one side. Othe side I want my name,number under owner operator and a list of what I do. , drainage,grading,trenching stump removal , postholes. Landscaping lawn renovations, and reconfigurations, small to large rip outs and installs,sod work and burms and swails for water run off and plantings the two pictures of cards is what I like
Updates

Project Deadline Extended
Reason: First time doing this not sure if two days was enough, no one was taking on project so trying to figure out why I posted a picture of what I want so should be relatively easy

Industry/Entity Type

Landscaping

Contact Information for Business Card

Name Ted Brisbo
Palm beach county Phone 860-555-0142

Font styles to use
Other font styles liked:
• It's on card I sent second one

Requirements
Must have
• Same colors and look of card at bottom
Nice to have
• All aspects of excavation and landscaping on back of card
• Will add web address at end

```html
<!DOCTYPE html>
<html lang="en">
<head>
<meta charset="utf-8">
<title>Brisbo Excavation and Landscaping – Business Card</title>
<link rel="stylesheet" href="https://fonts.googleapis.com/css2?family=Work+Sans:wght@400;500;700&display=swap">
<style>
  :root {
    --orange: #e07838;
    --ink: #2b2b2b;
    --paper: #ffffff;
    --backdrop: #e4e4e4;
    --shadow: rgba(0, 0, 0, 0.22);
  }
  * { box-sizing: border-box; margin: 0; padding: 0; }
  html, body {
    width: 1200px;
    height: 1000px;
    overflow: hidden;
    background: var(--backdrop);
    font-family: "Work Sans", Arial, sans-serif;
  }
  .sheet {
    position: relative;
    width: 1200px;
    height: 1000px;
  }
  .card {
    position: absolute;
    left: 250px;
    width: 700px;
    height: 400px;
    border-radius: 14px;
    overflow: hidden;
    box-shadow: 4px 6px 14px var(--shadow);
  }
  /* Front: contact side */
  .card-front {
    top: 60px;
    background: var(--paper);
  }
  .holder {
    position: absolute;
    left: 48px;
    top: 42px;
  }
  .holder-name {
    font-size: 26px;
    font-weight: 700;
    color: var(--orange);
    letter-spacing: 0.5px;
    text-transform: uppercase;
    line-height: 1.1;
  }
  .holder-role {
    font-size: 17px;
    font-weight: 500;
    color: var(--ink);
    text-transform: uppercase;
    margin-top: 4px;
  }
  .contacts {
    position: absolute;
    left: 48px;
    top: 170px;
    list-style: none;
  }
  .contacts li {
    display: flex;
    align-items: center;
    gap: 14px;
    font-size: 17px;
    color: var(--ink);
    height: 28px;
  }
  .contacts svg { width: 16px; height: 16px; flex: none; }
  .brand {
    position: absolute;
    right: 44px;
    top: 118px;
    display: flex;
    align-items: center;
    gap: 12px;
  }
  .brand-mark {
    width: 22px;
    height: 22px;
    background: var(--orange);
    flex: none;
  }
  .brand-name {
    font-size: 20px;
    font-weight: 700;
    color: var(--orange);
    text-transform: uppercase;
    line-height: 1.2;
    width: 250px;
  }
  .rule {
    position: absolute;
    left: 0;
    right: 0;
    top: 268px;
    height: 4px;
    background: var(--orange);
  }
  .services {
    position: absolute;
    left: 0;
    right: 0;
    bottom: 0;
    height: 122px;
    background: var(--orange);
    padding: 14px 48px;
    list-style: none;
  }
  .services li {
    font-size: 16px;
    color: var(--paper);
    line-height: 24px;
  }
  /* Back: brand side */
  .card-back {
    top: 540px;
    background: var(--orange);
    display: flex;
    align-items: center;
    justify-content: center;
  }
  .card-back .brand-name {
    color: var(--paper);
    font-size: 30px;
    width: auto;
    text-align: center;
  }
</style>
</head>
<body>
<main class="sheet">
  <section class="card card-front" aria-label="Business card front">
    <div class="holder">
      <p class="holder-name">Ted Brisbo</p>
      <p class="holder-role">Owner</p>
    </div>

    <ul class="contacts">
      <li>
        <svg viewBox="0 0 16 16" aria-hidden="true"><rect x="4" y="1" width="8" height="14" rx="1.5" fill="none" stroke="var(--orange)" stroke-width="1.6"/><circle cx="8" cy="12.3" r="0.9" fill="var(--orange)"/></svg>
        860-555-0142
      </li>
      <li>
        <svg viewBox="0 0 16 16" aria-hidden="true"><rect x="1" y="3" width="14" height="10" fill="var(--orange)"/><path d="M1 3 L8 9 L15 3" fill="none" stroke="#fff" stroke-width="1.2"/></svg>
        info@tedbrisbo.com
      </li>
      <li>
        <svg viewBox="0 0 16 16" aria-hidden="true"><circle cx="6.5" cy="6.5" r="4.3" fill="none" stroke="var(--orange)" stroke-width="2"/><line x1="9.6" y1="9.6" x2="14.5" y2="14.5" stroke="var(--orange)" stroke-width="2.4" stroke-linecap="round"/></svg>
        www.brisboexcavation.com
      </li>
    </ul>

    <div class="brand">
      <span class="brand-mark" aria-hidden="true"></span>
      <p class="brand-name">Brisbo Excavation and Landscaping</p>
    </div>

    <div class="rule" aria-hidden="true"></div>

    <ul class="services">
      <li>Drainage | Grading | Trenching | Stump removal | Postholes</li>
      <li>Landscaping lawn renovations | Reconfigurations</li>
      <li>Small to large rip outs and installs | Sod work and burms</li>
      <li>Swails for water run off and plantings</li>
    </ul>
  </section>

  <section class="card card-back" aria-label="Business card back">
    <p class="brand-name">Brisbo Excavation<br>and Landscaping</p>
  </section>
</main>
</body>
</html>
```